Banner Ad Design Project

We would like to create a banner for Velmora to attract designers to use our platform.
Guidelines:
Animated Banner (GIF)
50k max file size
Animation loops and stops after 30 secs
Design Instructions:
Design should be clean and based on the color schemes of the site: http://www.velmora-example.com/designer to get a sense of the site, fill the form.
Copy:
Are you a Designer?
Join velmora and earn money
Call to action:
Sign up NOW!
Updates
Banner size is 300*250
Project Deadline Extended

```html
<!DOCTYPE html>
<html lang="en">
<head>
<meta charset="utf-8">
<title>Velmora – Banner Set</title>
<link rel="stylesheet" href="https://fonts.googleapis.com/css2?family=Open+Sans:wght@700;800&display=swap">
<style>
  :root {
    --backdrop: #6b4529;
    --blue: #3d9be0;
    --crimson: #c8174f;
    --lime: #8ab93e;
    --band: #2f2f2f;
    --white: #ffffff;
    --glyph-shadow: rgba(0, 0, 0, 0.35);
  }
  * { margin: 0; padding: 0; box-sizing: border-box; }
  html, body {
    width: 1200px;
    height: 838px;
    overflow: hidden;
    background: var(--backdrop);
    font-family: "Open Sans", Arial, sans-serif;
  }
  .banner-set {
    position: relative;
    width: 1200px;
    height: 838px;
  }
  .banner {
    position: absolute;
    top: 255px;
    width: 366px;
    height: 305px;
    box-shadow: 0 4px 10px rgba(0, 0, 0, 0.45);
    overflow: hidden;
  }
  .banner--question { left: 29px; --accent: var(--blue); }
  .banner--join { left: 413px; --accent: var(--crimson); }
  .banner--earn { left: 794px; --accent: var(--lime); }

  .banner__panel {
    position: absolute;
    left: 0; top: 0;
    width: 366px;
    height: 244px;
    background: var(--accent);
    overflow: hidden;
  }
  .banner__headline {
    position: absolute;
    z-index: 2;
    color: var(--white);
    font-weight: 700;
    font-size: 30px;
    line-height: 34px;
    text-transform: uppercase;
    white-space: nowrap;
  }
  .banner--question .banner__headline { left: 26px; top: 18px; text-align: left; }
  .banner--join .banner__headline { left: 0; width: 350px; top: 112px; text-align: center; }
  .banner--earn .banner__headline { left: 0; width: 356px; top: 80px; line-height: 39px; text-align: center; }

  .banner__mark {
    position: absolute;
    z-index: 1;
    top: -38px;
    color: var(--white);
    font-weight: 800;
    font-size: 300px;
    line-height: 1;
    text-shadow: -3px -3px 4px var(--glyph-shadow);
    transform-origin: right center;
  }
  .banner--question .banner__mark { right: 11px; transform: scaleX(0.72); }
  .banner--join .banner__mark { right: 23px; transform: scaleX(0.62); }
  .banner--earn .banner__mark { right: 26px; transform: scaleX(0.62); }

  .banner__band {
    position: absolute;
    left: 0; bottom: 0;
    width: 366px;
    height: 61px;
    background: var(--band);
    display: flex;
    align-items: center;
  }
  .brand-name {
    margin-left: 38px;
    width: 132px;
    color: var(--white);
    font-weight: 700;
    font-size: 26px;
    letter-spacing: -0.5px;
  }
  .cta {
    display: flex;
    align-items: center;
    gap: 8px;
    color: var(--white);
    font-weight: 700;
    font-size: 16px;
    text-transform: uppercase;
  }
  .cta__chevrons { width: 16px; height: 14px; }
  .cta__chevrons path {
    fill: none;
    stroke: var(--accent);
    stroke-width: 2.6;
    stroke-linecap: square;
  }
</style>
</head>
<body>
<main class="banner-set">

  <section class="banner banner--question">
    <div class="banner__panel">
      <h2 class="banner__headline">Are you<br>a designer</h2>
      <span class="banner__mark" aria-hidden="true">?</span>
    </div>
    <footer class="banner__band">
      <span class="brand-name">velmora</span>
      <span class="cta">
        <svg class="cta__chevrons" viewBox="0 0 16 14" aria-hidden="true"><path d="M2 2 L6 7 L2 12 M9 2 L13 7 L9 12"/></svg>
        Sign up now
        <svg class="cta__chevrons" viewBox="0 0 16 14" aria-hidden="true"><path d="M7 2 L3 7 L7 12 M14 2 L10 7 L14 12"/></svg>
      </span>
    </footer>
  </section>

  <section class="banner banner--join">
    <div class="banner__panel">
      <h2 class="banner__headline">Join us</h2>
      <span class="banner__mark" aria-hidden="true">!</span>
    </div>
    <footer class="banner__band">
      <span class="brand-name">velmora</span>
      <span class="cta">
        <svg class="cta__chevrons" viewBox="0 0 16 14" aria-hidden="true"><path d="M2 2 L6 7 L2 12 M9 2 L13 7 L9 12"/></svg>
        Sign up now
        <svg class="cta__chevrons" viewBox="0 0 16 14" aria-hidden="true"><path d="M7 2 L3 7 L7 12 M14 2 L10 7 L14 12"/></svg>
      </span>
    </footer>
  </section>

  <section class="banner banner--earn">
    <div class="banner__panel">
      <h2 class="banner__headline">And<br>earn money</h2>
      <span class="banner__mark" aria-hidden="true">!</span>
    </div>
    <footer class="banner__band">
      <span class="brand-name">velmora</span>
      <span class="cta">
        <svg class="cta__chevrons" viewBox="0 0 16 14" aria-hidden="true"><path d="M2 2 L6 7 L2 12 M9 2 L13 7 L9 12"/></svg>
        Sign up now
        <svg class="cta__chevrons" viewBox="0 0 16 14" aria-hidden="true"><path d="M7 2 L3 7 L7 12 M14 2 L10 7 L14 12"/></svg>
      </span>
    </footer>
  </section>

</main>
</body>
</html>
```